Desing for real estate offers- Package system

The word should be graphically clear and understandable. There are 3 packages that the customer can buy: the basic package is red, the medicinal package is green and the carefree package is blue. See the Word document in the appendix. End file should be a Word, as we need to chance the text. It should also match the website as well as the business card.
https://brelunor.vantosite.ch/
Colors:
Green 1: R: 187, G: 214, B: 49
Green 2: R: 119, G: 187, W: 66

Target Market(s)

Real estate company

Font styles to use
Serif
Sans Serif

```html
<!DOCTYPE html>
<html lang="de">
<head>
<meta charset="utf-8">
<title>Brelunor – Verkaufspakete</title>
<link href="https://fonts.googleapis.com/css2?family=Archivo+Black&family=Barlow:ital,wght@0,400;0,500;0,600;1,500&family=Arimo&display=swap" rel="stylesheet">
<style>
:root{
  --green-1:#bbd631;
  --green-2:#77bb42;
  --heading-green:#a9d18e;
  --panel:#e2f0d9;
  --ink:#1a1a1a;
  --page-bg:#e9e9e9;
  --paper:#ffffff;
  --contact-bg:#f8f8f8;
}
*{margin:0;padding:0;box-sizing:border-box}
html,body{width:1200px;height:1015px;overflow:hidden;background:var(--page-bg)}
body{position:relative;font-family:"Barlow",sans-serif;color:var(--ink)}
.sheet{position:absolute;left:261px;top:27px;width:678px;height:960px;
  background:linear-gradient(135deg,#cfe27a 0%,var(--green-1) 45%,var(--green-2) 100%);}
.paper{position:absolute;left:22px;top:10px;right:22px;bottom:9px;background:var(--paper)}
.sheet-inner{position:absolute;inset:0}
.brand{position:absolute;left:38px;top:42px;font-family:"Barlow",sans-serif;font-weight:600;font-size:26px;color:var(--green-2);letter-spacing:.3px}
.contact{position:absolute;left:422px;top:28px;width:217px;height:62px;background:var(--contact-bg);
  font-family:"Arimo",sans-serif;font-size:12px;line-height:15.5px;padding:7px 0 0 8px}
.contact li{list-style:none;display:flex;align-items:center;gap:5px}
.contact svg{width:11px;height:11px;flex:none}
.prices{position:absolute;left:0;right:0;top:125px;text-align:center;font-size:12.6px;font-weight:500;line-height:26px}
.pkg-title{position:absolute;font-family:"Archivo Black",sans-serif;color:var(--heading-green);font-size:40px;line-height:1;letter-spacing:.5px}
.pkg-box{position:absolute;background:var(--panel);font-size:12.6px;font-weight:500;line-height:19px}
.pkg-box .lead{padding:7px 0 0 9px;margin-bottom:10px}
.pkg-box ul{padding-left:50px}
.pkg-box li{padding-left:2px}
.basis-title{left:45px;top:228px}
.basis-box{left:45px;top:263px;width:291px;height:343px;padding-top:5px}
.basis-box ul{width:285px}
.medicinal-title{left:345px;top:230px}
.medicinal-box{left:346px;top:265px;width:290px;height:341px}
.medicinal-box ul{padding-left:50px;padding-right:8px}
.carefree-title{left:50px;top:621px}
.carefree-box{left:45px;top:656px;width:591px;height:208px}
.note{position:absolute;left:0;right:0;top:895px;text-align:center;font-style:italic;font-weight:500;font-size:11.6px;line-height:16px}
</style>
</head>
<body>
<main class="sheet">
  <div class="paper"></div>
  <div class="sheet-inner">
    <div class="brand">Brelunor</div>
    <ul class="contact">
      <li><svg viewBox="0 0 12 12"><circle cx="6" cy="6" r="6" fill="#77bb42"/><path d="M4 3.2l1 1.2-.6.7c.4.9 1 1.5 1.9 1.9l.7-.6 1.2 1-.6.9C5.6 8 4 6.4 3.6 4.1z" fill="#fff"/></svg>044 610 27 39</li>
      <li><svg viewBox="0 0 12 12"><circle cx="6" cy="6" r="6" fill="#77bb42"/><rect x="3" y="4" width="6" height="4.2" rx=".6" fill="#fff"/><path d="M3.3 4.3L6 6.3l2.7-2" stroke="#77bb42" stroke-width=".7" fill="none"/></svg>lena.vogt@brelunor.ch</li>
      <li><svg viewBox="0 0 12 12"><circle cx="6" cy="6" r="6" fill="#77bb42"/><circle cx="6" cy="6" r="3" fill="none" stroke="#fff" stroke-width=".8"/><path d="M3 6h6M6 3c-1.3 1.6-1.3 4.4 0 6M6 3c1.3 1.6 1.3 4.4 0 6" stroke="#fff" stroke-width=".6" fill="none"/></svg>brelunor.vantosite.ch</li>
    </ul>

    <div class="prices">
      <p>Basis-Paket 8'500.- CHF exkl. MWST</p>
      <p>Medium-Paket 10'900 CHF exkl. MWST</p>
      <p>Sorglos: 2% vom Verkaufspreis inkl. MWST (von Grundstückgewinnsteuer abziehbar)</p>
    </div>

    <h2 class="pkg-title basis-title">BASIS</h2>
    <section class="pkg-box basis-box">
      <ul>
        <li>Begehung Verkaufsobjekt</li>
        <li>Hedonische Schätzung intern &amp; Bank</li>
        <li>Marketing &amp; Vertriebskonzept</li>
        <li>Unterlagen einfordern- STWEG Protokolle, GB Auszug u.s.w wenn nötig</li>
        <li>Fotografieren &amp; Ausmessen der Immobilie</li>
        <li>Grundriss zeichnen</li>
        <li>Dokumentation erstellen</li>
        <li>Immobilie Online aufbereiten &amp; Aufschalten</li>
        <li>Interessenten &amp; Kaufangebote prüfen</li>
        <li>Käufer zusage- andere noch vertrösten</li>
        <li>Erstellung erster Kaufvertragsentwurf</li>
      </ul>
    </section>

    <h2 class="pkg-title medicinal-title">MEDICINAL</h2>
    <section class="pkg-box medicinal-box">
      <p class="lead">Basis Paket +</p>
      <ul>
        <li>Unsere Interessenten anschreiben</li>
        <li>Anfragen beantworten- telefonisch &amp; elektronisch</li>
        <li>Evt. Bieterverfahren modern oder altmodisch</li>
        <li>Begleitung aufs Notariat</li>
      </ul>
    </section>

    <h2 class="pkg-title carefree-title">CAREFREE</h2>
    <section class="pkg-box carefree-box">
      <p class="lead">Medium Paket +</p>
      <ul>
        <li>Besichtigungen koordinieren</li>
        <li>Besichtigungen Durchführen</li>
        <li>Sicherheitsnachweis (SINA)- organisieren</li>
        <li>Erstellung erster Kaufvertragsentwurf</li>
        <li>Berechnung provisorische Grundstückgewinnsteuer- Steueramt</li>
        <li>Beurkundungstermin vereinbaren</li>
        <li>Eigentumsübertragung vereinbaren</li>
        <li>Helfen bei der Steuererklärung für die definitive Grundstückgewinnsteuer</li>
      </ul>
    </section>

    <p class="note">Unterlagen müssen gestellt werden, ansonsten werden Sie 1:1 verrechnet: GB-Auszug,GVZ,<br>Nebenkostenabrechnung, STWEG-Protokolle der letzten 3 Jahren, …</p>
  </div>
</main>
</body>
</html>
```